Moroccan Argan Oil label for hair care products

We need a label design for our brand Velnora.
The products are for hair care: Conditoner and Shampoo. We prefer fruit as graphics. The caps of the bottle will be light/apple green, the bottles are white opaque. The label color should be green and/or red/orange. Text on the front side: Moroccan Argan Oil, Shampoo, Strengthens, Hydrates, 474 ml
Please find attached label size.pdf and the bottle. Label size: 50x140 mm.
As the bottles are oval we need one front and one back label.
People in Europe, also african people
Hair

```html
<!DOCTYPE html>
<html lang="en">
<head>
<meta charset="utf-8">
<title>Velnora – Moroccan Argan Oil Shampoo Label</title>
<link rel="stylesheet" href="https://fonts.googleapis.com/css2?family=Cinzel:wght@400;600&display=swap">
<style>
  :root {
    --backdrop: #2a0e0c;
    --label-black: #141210;
    --gold: #c9a15a;
    --gold-deep: #9c7534;
    --cream: #efe3c6;
  }
  html, body {
    margin: 0;
    width: 1200px;
    height: 1200px;
    overflow: hidden;
    background: var(--backdrop);
  }
  .canvas {
    width: 1200px;
    height: 1200px;
    display: flex;
    align-items: center;
    justify-content: center;
  }
  .front-label {
    width: 440px;
    height: 980px;
    display: block;
  }
  .label-body { fill: var(--label-black); }
  .label-rim { fill: none; stroke: var(--gold); stroke-width: 5; }
  .label-rim-inner { fill: none; stroke: var(--gold-deep); stroke-width: 1.5; }
  .benefit {
    font-family: "Cinzel", serif;
    font-size: 27px;
    font-weight: 400;
    fill: var(--cream);
    letter-spacing: 1px;
  }
  .arc-word {
    font-family: "Cinzel", serif;
    font-size: 30px;
    font-weight: 400;
    fill: var(--gold);
    letter-spacing: 4px;
  }
  .product-name {
    font-family: "Cinzel", serif;
    font-size: 50px;
    font-weight: 400;
    fill: var(--cream);
    letter-spacing: 1px;
  }
  .brand-name {
    font-family: "Cinzel", serif;
    font-size: 30px;
    font-weight: 400;
    fill: var(--gold);
    letter-spacing: 2px;
  }
  .volume {
    font-family: "Cinzel", serif;
    font-size: 30px;
    font-weight: 400;
    fill: var(--gold);
    letter-spacing: 2px;
  }
  .accent-dot { fill: var(--gold); }
  .ornament-area { fill: url(#ornamentTone); }
</style>
</head>
<body>
<main class="canvas">
  <svg class="front-label" viewBox="0 0 440 980" xmlns="http://www.w3.org/2000/svg" aria-label="Velnora Moroccan Argan Oil Shampoo front label">
    <defs>
      <linearGradient id="ornamentTone" x1="0" y1="0" x2="0" y2="1">
        <stop offset="0" stop-color="#d8b36b"/>
        <stop offset="1" stop-color="#9c7534"/>
      </linearGradient>
      <path id="arcTop" d="M 95 395 A 140 140 0 0 1 345 395"/>
      <path id="arcBottom" d="M 95 535 A 140 140 0 0 0 345 535"/>
    </defs>

    <ellipse class="label-body" cx="220" cy="490" rx="212" ry="482"/>
    <ellipse class="label-rim" cx="220" cy="490" rx="206" ry="476"/>
    <ellipse class="label-rim-inner" cx="220" cy="490" rx="196" ry="466"/>

    <text class="benefit" x="220" y="160" text-anchor="middle">HYDRATES</text>
    <text class="benefit" x="220" y="200" text-anchor="middle">STRENGTHENS</text>

    <text class="arc-word" text-anchor="middle">
      <textPath href="#arcTop" startOffset="50%">MOROCCAN</textPath>
    </text>
    <circle class="accent-dot" cx="88" cy="392" r="4"/>
    <circle class="accent-dot" cx="352" cy="392" r="4"/>

    <g role="img" aria-label="Gold scrollwork flourish above the product name">
      <rect class="ornament-area" x="100" y="372" width="240" height="40" rx="20"/>
    </g>

    <text class="product-name" x="220" y="466" text-anchor="middle">ARGAN OIL</text>

    <g role="img" aria-label="Gold scrollwork flourish below the product name">
      <rect class="ornament-area" x="100" y="496" width="240" height="40" rx="20"/>
    </g>

    <circle class="accent-dot" cx="88" cy="545" r="4"/>
    <circle class="accent-dot" cx="352" cy="545" r="4"/>
    <text class="arc-word" text-anchor="middle">
      <textPath href="#arcBottom" startOffset="50%">SHAMPOO</textPath>
    </text>

    <text class="brand-name" x="220" y="745" text-anchor="middle">VELNORA</text>

    <text class="volume" x="220" y="850" text-anchor="middle">474 ML</text>
  </svg>
</main>
</body>
</html>
```